Heron valley RV Resort business card

I need a design card for the logo I just had made on here. I will provide it and please make some cool designs, thank you.

I would like the card to have
- phone number (865-318-2967)
- email ( heronvalleyrv@pinemail.com)
- address to the park ( 5186 Quarry Gate Loop rd, Maryville, TN) ZIP: 37429
on the back for double sided id like some lines for writing on. thanks

please follow the logo we provided in the files, I can provide the photoshop file if you need it.

please note this is in the Smokey mountains of Tennessee

Target Market(s)

cabin/rv rentals

Industry/Entity Type

rv/campground/cabin rentals

Contact Information for Business Card

address/email/phone number I added details in brief

Requirements
Must have
• on the back add a bear or something cool

```html
<!DOCTYPE html>
<html lang="en">
<head>
<meta charset="utf-8">
<title>Heron Valley RV Resort — Business Card</title>
<link rel="stylesheet" href="https://fonts.googleapis.com/css2?family=Montserrat:wght@400&display=swap">
<style>
  :root {
    --backdrop: #2a2a2a;
    --card: #ffffff;
    --ink: #111510;
    --rule: #3a3a3a;
    --mark: #5a7ea8;
  }
  * { margin: 0; padding: 0; box-sizing: border-box; }
  html, body {
    width: 1200px;
    height: 782px;
    overflow: hidden;
    background: var(--backdrop);
  }
  .canvas {
    position: relative;
    width: 1200px;
    height: 782px;
  }
  .card {
    position: absolute;
    top: 238px;
    width: 508px;
    height: 305px;
    background: var(--card);
    font-family: "Montserrat", sans-serif;
    color: var(--ink);
  }
  .card--back { left: 76px; }
  .card--front { left: 616px; }

  .brand {
    position: absolute;
    display: flex;
    flex-direction: column;
    align-items: center;
    gap: 10px;
    color: var(--ink);
    font-family: "Montserrat", sans-serif;
    font-weight: 400;
    text-align: center;
  }
  .brand__dot {
    flex: none;
    border-radius: 50%;
    background: var(--mark);
  }
  .card--back .brand { left: 48px; width: 180px; top: 72px; font-size: 19px; line-height: 1.2; }
  .card--back .brand__dot { width: 118px; height: 118px; }
  .card--front .brand { left: 61px; width: 140px; top: 84px; font-size: 15px; line-height: 1.2; }
  .card--front .brand__dot { width: 90px; height: 90px; }

  .write-lines {
    position: absolute;
    left: 260px;
    width: 199px;
    top: 146px;
  }
  .write-lines__line {
    position: absolute;
    left: 0;
    width: 100%;
    border-top: 1px dashed var(--rule);
  }

  .contact {
    position: absolute;
    left: 226px;
    top: 108px;
    right: 0;
    height: 89px;
    border-bottom: 1px solid var(--ink);
  }
  .contact__bar {
    position: absolute;
    left: 0;
    top: 0;
    width: 17px;
    height: 89px;
    background: var(--ink);
    border-radius: 3px 3px 0 0;
  }
  .contact__icon {
    position: absolute;
    left: 3px;
    width: 11px;
    height: 11px;
    fill: #fff;
  }
  .contact__text {
    position: absolute;
    left: 21px;
    font-size: 12.6px;
    line-height: 15px;
    letter-spacing: 0.1px;
    white-space: nowrap;
  }
</style>
</head>
<body>
<main class="canvas">

  <section class="card card--back" aria-label="Card back with writing lines">
    <div class="brand">
      <span class="brand__dot"></span>
      <span class="brand__name">Heron Valley<br>RV Resort</span>
    </div>
    <div class="write-lines" aria-label="Lines for writing">
      <span class="write-lines__line" style="top:0"></span>
      <span class="write-lines__line" style="top:32px"></span>
      <span class="write-lines__line" style="top:62px"></span>
    </div>
  </section>

  <section class="card card--front" aria-label="Card front with contact details">
    <div class="brand">
      <span class="brand__dot"></span>
      <span class="brand__name">Heron Valley<br>RV Resort</span>
    </div>
    <div class="contact">
      <div class="contact__bar">
        <svg class="contact__icon" style="top:10px" viewBox="0 0 24 24" aria-hidden="true">
          <path d="M6.6 10.8a15.1 15.1 0 0 0 6.6 6.6l2.2-2.2a1 1 0 0 1 1-.25 11.4 11.4 0 0 0 3.6.57 1 1 0 0 1 1 1V20a1 1 0 0 1-1 1A17 17 0 0 1 3 4a1 1 0 0 1 1-1h3.5a1 1 0 0 1 1 1c0 1.250.2 2.450.57 3.570a1 1 0 0 1-.25 1z"/>
        </svg>
        <svg class="contact__icon" style="top:33px" viewBox="0 0 24 24" aria-hidden="true">
          <path d="M2 5h20v14H2z M3.5 6.5 12 13l8.5-6.5" fill="none" stroke="#fff" stroke-width="2"/>
        </svg>
        <svg class="contact__icon" style="top:55px" viewBox="0 0 24 24" aria-hidden="true">
          <path d="M12 3 1 12h3v9h6v-6h4v6h6v-9h3z"/>
        </svg>
      </div>
      <p class="contact__text" style="top:8px">865-318-2967</p>
      <p class="contact__text" style="top:31px">heronvalleyrv@pinemail.com</p>
      <p class="contact__text" style="top:53px">5186 Quarry Gate Loop rd, Maryville,<br>TN ZIP: 37429</p>
    </div>
  </section>

</main>
</body>
</html>
```